Layout für Broschüre für chemiefreie Lösung, Kühlwasser aufzubereiten
Zielgruppe
VELTROMAX hat eine Technologie entwickelt, die in der Industrie eingesetzt wird um in geschlossenen und offenen Kühlkreisläufen ohne Biozide und Korrosion Inhibitoren das Kühlwasser aufzubereiten. Mit VELTROMAX haben die Unternehmen eine chemiefreie Lösungen gegen Biofouling, Korrosion und Kalk. Zielgruppe sind alle Unternehmen die etwas produzieren oder Klimaanlagen / Heizungssysteme betreiben. Es geht um zukunftsorientierte und vor allem nachhaltige Technologie ohne Einsatz von Chemie.
Aufgabenstellung
Wir suchen für die Broschüre ein neues Layout, dass geradlinig und klar strukturiert ist, vor allem modern. Die Broschüre sollte DIN A 4 - Format sein in der gewohnten Struktur Umschlagseite innen und außen und 8 - 10 Innenseiten. Im Layout sollte ein roter Faden zu erkennen sein, aber nicht jede Seite gleich aussehen. Die Anlagen sind nur beispielhaft vom bestehenden Material und sollten vom Layout keinesfalls eine Orientierung geben, denn das soll verändert werden. Die Anlagen sind für einen inhaltlichen Überblick.

```html
<!DOCTYPE html>
<html lang="de">
<head>
<meta charset="utf-8">
<title>Klarfluss – Inhalt und Vorwort</title>
<link href="https://fonts.googleapis.com/css2?family=Heebo:wght@300;400;500&display=swap" rel="stylesheet">
<style>
  :root {
    --backdrop: #dcdcda;
    --paper: #f7f7f4;
    --navy: #15113a;
    --frame: #1e1a4a;
    --teal: #3fb8c8;
    --label-bg: #3c3e3b;
    --ink: #1d1d1d;
    --ink-soft: #4a4a4a;
    --rule: #c9c9c5;
    --toc-ink: #a9a7c2;
  }
  * { margin: 0; padding: 0; box-sizing: border-box; }
  html, body { width: 1200px; height: 900px; overflow: hidden; }
  body {
    background: var(--backdrop);
    font-family: "Heebo", Arial, sans-serif;
    color: var(--ink);
    position: relative;
  }
  .spread {
    position: absolute;
    left: 77px; top: 80px;
    width: 1046px; height: 740px;
    display: flex;
    box-shadow: 0 6px 24px rgba(0,0,0,0.12);
  }
  .page {
    position: relative;
    width: 523px; height: 740px;
    background: var(--paper);
    overflow: hidden;
  }

  /* left page */
  .intro {
    position: absolute;
    left: 40px; top: 112px;
    width: 118px;
    text-align: right;
  }
  .intro-title {
    font-size: 11px; font-weight: 500;
    letter-spacing: 0.02em;
    margin-bottom: 12px;
  }
  .intro p {
    font-size: 6.6px; line-height: 1.55;
    color: var(--ink-soft);
    margin-bottom: 9px;
  }
  .contents {
    position: absolute;
    left: 181px; top: 107px;
    width: 342px; height: 633px;
    background: var(--navy);
  }
  .contents-title {
    position: absolute;
    left: 22px; top: 24px;
    color: var(--teal);
    font-size: 20px; font-weight: 400;
    letter-spacing: 0.04em;
  }
  .toc { list-style: none; }
  .toc li {
    position: absolute;
    left: 56px; width: 203px;
    display: flex; justify-content: space-between;
    font-size: 8px; font-weight: 300;
    color: var(--toc-ink);
    letter-spacing: 0.03em;
  }
  .toc li:nth-child(1) { top: 77px; }
  .toc li:nth-child(2) { top: 119px; }
  .toc li:nth-child(3) { top: 162px; }

  .folio {
    position: absolute; top: 706px;
    font-size: 7px; color: var(--ink-soft);
    padding-top: 4px;
    border-top: 1px solid var(--rule);
  }
  .folio-left { left: 40px; width: 141px; }
  .folio-right { right: 40px; width: 470px; text-align: right; }

  /* right page */
  .foreword {
    position: absolute;
    left: 99px; top: 218px;
    width: 319px; height: 347px;
    border: 2px solid var(--frame);
  }
  .foreword-label {
    position: absolute;
    left: 79px; top: -12px;
    width: 157px; height: 34px;
    background: var(--label-bg);
    box-shadow: 0 0 0 8px var(--paper);
    color: var(--teal);
    font-size: 20px; font-weight: 400;
    letter-spacing: 0.08em;
    display: flex; align-items: center; justify-content: center;
  }
  .foreword-body {
    position: absolute;
    left: 37px; top: 76px;
    width: 246px;
  }
  .foreword-body p {
    font-size: 12px; line-height: 1.08;
    font-weight: 300;
    margin-bottom: 10px;
  }
</style>
</head>
<body>
  <main class="spread">
    <section class="page page-left">
      <div class="intro">
        <h2 class="intro-title">OTASPED QUE</h2>
        <p>Ut tenitatas volum que quiaamus ma dolum es endelens eumquate pona por rehenimus, ut asit, qui ut quiatet laccae exerior aut reseqai utaptas et remo con plandae.</p>
        <p>Caram a dolo tria venet mo comnis modi et volorpo relessunt que minctur, quiassimusam que as quiatem et, id ent quam as volupta.</p>
      </div>
      <nav class="contents">
        <h1 class="contents-title">INHALT</h1>
        <ol class="toc">
          <li><span>3</span><span>KAPITEL 1</span></li>
          <li><span>4</span><span>KAPITEL 2</span></li>
          <li><span>8</span><span>KAPITEL3</span></li>
        </ol>
      </nav>
      <div class="folio folio-left">2 Klarfluss</div>
    </section>

    <section class="page page-right">
      <article class="foreword">
        <h2 class="foreword-label">VORWORT</h2>
        <div class="foreword-body">
          <p>Pa sus dellore stiunt, comnis alis aut ullent dolupta esequia dolupta sinullant por magnimin pellentio. Nam, nossunt quibus eumquunt es aborecea comnima gnianda ecepudaectur am fugiatu resecum in nonempo rerumqu iatatur?</p>
          <p>Nam recudam quid ma quis ab istius esequae nonem quas sa dolupta que pligend igendem dem vitiosam ex excerionsed maximpo rerciatSequi di sum quiassi tatem. Itam nis aut et vendign isciatu restistrum, sandae ipsam suntio oditenda consedist imus.</p>
          <p>Enia corisciae mos quis et molecep rorest,</p>
        </div>
      </article>
      <div class="folio folio-right">Klarfluss 3</div>
    </section>
  </main>
</body>
</html>
```